販促の一環として、「初回限定無料お試しキャンペーン」を行います。

つきましてはトップバナーx1枚(960 x 500)※若干変更の可能性あり
ピコルン広告用バナー x1枚
計2枚の制作をお願い致します。

※ピコルン広告用バナーには添付の弊社ロゴも入れて頂ければ助かります。
(必須ではなくデザイン的に入れない方が良い場合は外して頂いて問題ありません。)

【添付】
なんとなく気に入ったものを無作為に載せました。
(ご参考として。)
・初回限定無料お試しキャンペーン
(上記内容が伝われば表記は問いません。)
・期間:2022/7/31まで
• 960x500

シンプルながらも細部まで手の込んだデザインが大変気に入りました。

この度は素晴らしいご提案を多数頂き、誠にありがとうございました。
今後もバナー制作をコンペ形式でお願いすることがございますので、
その際はご応募頂けますと幸いです。

```html
<!DOCTYPE html>
<html lang="ja">
<head>
<meta charset="utf-8">
<title>ゴルフウェアレンタルサービス 初回限定無料お試しキャンペーン</title>
<link href="https://fonts.googleapis.com/css2?family=Noto+Sans+JP:wght@500;700;900&display=swap" rel="stylesheet">
<style>
  :root{
    --mint:#a9e2cb;
    --mint-light:#e6f7ef;
    --green-dark:#2d7a5c;
    --ink:#333333;
    --red:#e5232b;
    --yellow:#f5d633;
    --yellow-dark:#d9b51c;
    --white:#ffffff;
  }
  *{margin:0;padding:0;box-sizing:border-box}
  html,body{width:781px;height:1200px;overflow:hidden;background:var(--white)}
  body{position:relative;font-family:"Noto Sans JP",sans-serif;color:var(--ink)}
  .banner{position:absolute;left:0;width:781px;overflow:hidden;
    background:radial-gradient(ellipse at 50% 55%,var(--white) 0%,var(--mint-light) 40%,var(--mint) 100%)}
  .banner--top{top:0;height:380px}
  .banner--ad{top:410px;height:790px}
  .abs{position:absolute}
  .center{left:0;right:0;text-align:center}

  .top-heading{top:0;left:0;right:0;height:52px;background:var(--white);
    font-weight:700;font-size:30px;letter-spacing:3px;color:var(--ink);text-align:center;line-height:52px}

  .badge{border-radius:50%;background:var(--red);color:var(--white);font-weight:700;
    display:flex;align-items:center;justify-content:center;text-align:center;line-height:1.15;
    border:4px solid var(--white);box-shadow:0 0 0 2px var(--red)}
  .badge--top{left:36px;top:78px;width:94px;height:94px;font-size:24px}
  .badge--ad{left:26px;top:230px;width:118px;height:118px;font-size:32px}

  .free{font-weight:900;color:var(--red);line-height:1}
  .free--top{top:92px;left:180px;width:240px;text-align:center;font-size:100px;letter-spacing:12px;padding-left:12px}
  .free--ad{top:338px;font-size:130px;letter-spacing:30px;padding-left:30px}

  .trial{font-weight:700;color:var(--red);letter-spacing:2px;line-height:1}
  .trial--top{top:212px;left:150px;width:300px;text-align:center;font-size:26px}
  .trial--ad{top:489px;font-size:36px}

  .note{left:520px;top:88px;width:180px;padding:10px 8px;background:var(--white);border-radius:10px;
    font-size:15px;line-height:1.6;color:var(--ink);text-align:center}

  .ribbon{display:block}
  .ribbon--top{left:70px;top:245px;width:640px;height:82px}
  .ribbon--ad{left:20px;top:540px;width:741px;height:96px}
  .date{font-weight:500;color:var(--ink);letter-spacing:2px;text-align:center;line-height:1}
  .date--top{left:70px;width:640px;top:268px;font-size:30px}
  .date--ad{left:20px;width:741px;top:566px;font-size:40px}

  .lead{top:36px;font-size:32px;font-weight:500;color:var(--ink);letter-spacing:2px;line-height:1.2}
  .service{top:76px;font-size:44px;font-weight:700;color:var(--ink);letter-spacing:6px;line-height:1.3}

  .brand{right:28px;bottom:22px;display:flex;align-items:center;gap:10px}
  .brand-mark{width:22px;height:22px;border-radius:50%;background:var(--green-dark)}
  .brand-name{font-weight:900;font-size:38px;color:var(--green-dark);letter-spacing:1px;line-height:1}
</style>
</head>
<body>

<section class="banner banner--top" aria-label="トップバナー">
  <h1 class="abs top-heading">ゴルフウェアレンタルサービス</h1>
  <div class="abs badge badge--top">初回<br>限定</div>
  <p class="abs free free--top">無料</p>
  <p class="abs trial trial--top">お試しキャンペーン</p>
  <p class="abs note">最新トレンドを<br>お手頃価格で!</p>
  <svg class="abs ribbon ribbon--top" viewBox="0 0 640 82" aria-hidden="true">
    <polygon points="0,20 48,20 48,76 0,76 16,48" fill="var(--yellow-dark)"/>
    <polygon points="640,20 592,20 592,76 640,76 624,48" fill="var(--yellow-dark)"/>
    <polygon points="32,6 608,6 608,66 32,66" fill="var(--yellow)"/>
  </svg>
  <p class="abs date date--top">2022/7/31まで</p>
</section>

<section class="banner banner--ad" aria-label="広告用バナー">
  <p class="abs center lead">最新トレンドをお手頃価格で!</p>
  <h2 class="abs center service">ゴルフウェア<br>レンタルサービス</h2>
  <div class="abs badge badge--ad">初回<br>限定</div>
  <p class="abs center free free--ad">無料</p>
  <p class="abs center trial trial--ad">お試しキャンペーン</p>
  <svg class="abs ribbon ribbon--ad" viewBox="0 0 741 96" aria-hidden="true">
    <polygon points="0,24 56,24 56,92 0,92 20,58" fill="var(--yellow-dark)"/>
    <polygon points="741,24 685,24 685,92 741,92 721,58" fill="var(--yellow-dark)"/>
    <polygon points="38,6 703,6 703,80 38,80" fill="var(--yellow)"/>
  </svg>
  <p class="abs date date--ad">2022/7/31まで</p>
  <div class="abs brand">
    <span class="brand-mark"></span>
    <span class="brand-name">TEE STYLE</span>
  </div>
</section>

</body>
</html>
```